Wordpress template re-design of current website

We need a WordPress template design and new look for our existing website. Our existing site it located at www.velomor.com.au We are a tech company and want a fresh, clean modern website that matches our brand, services and logo colors. Our main Services are hospitality solutions, Velomor TV solution and managed networks, more information on these can come from our existing website.

Target Market(s)

We are a tech company so must have a modern feel for new technology

Industry/Entity Type

It Company

Number of Pages Required

5+ page

Font styles to use
Sans Serif

Requirements
Must have
• Be based on a wordpress templete design and match the services that we have in our existing website, in the testimonials want a place for video testimonials as well as text. Nice clean icons used for graphics to represent services.
Nice to have
• nice visual representation of our services in the way of clean icons etc
Should not have
• Clutter

```html
<!DOCTYPE html>
<html lang="en">
<head>
<meta charset="utf-8">
<title>Velomor Wireless Internet</title>
<link rel="stylesheet" href="https://fonts.googleapis.com/css2?family=Open+Sans:wght@300;400;600;700;800&display=swap">
<style>
:root{
  --brand:#0b52a8;
  --brand-dark:#0c4a8e;
  --footer:#4f7fbf;
  --footer-line:#27497a;
  --ink:#333;
  --black:#0a0a0a;
  --white:#fff;
  --muted:#d9e4f3;
}
*{box-sizing:border-box;margin:0;padding:0}
html,body{width:1200px;height:4500px;overflow:hidden}
body{position:relative;font-family:"Open Sans",Arial,sans-serif;color:var(--ink);background:var(--white)}
.abs{position:absolute}

/* header */
.topbar{left:0;top:0;width:1200px;height:84px;background:var(--black)}
.brand-box{left:100px;top:0;width:215px;height:105px;background:var(--white);display:flex;align-items:center;justify-content:center;gap:10px}
.brand-mark{width:22px;height:22px;border-radius:50%;background:var(--brand);flex:none}
.brand-name{font-weight:700;font-size:34px;color:var(--brand);line-height:1;display:block}
.brand-tag{font-size:12px;color:var(--brand);display:block;margin-top:2px;letter-spacing:.5px}
.nav{left:330px;top:0;height:84px;display:flex;align-items:center;gap:26px;list-style:none}
.nav li{color:var(--white);font-size:15px;font-weight:600;letter-spacing:.5px}
.nav li.active{color:var(--brand)}
.phone{right:40px;top:0;height:84px;display:flex;align-items:center;gap:10px;color:var(--white);font-size:16px;font-weight:600}

/* hero */
.hero{left:0;top:84px;width:1200px;height:831px;background:var(--brand)}
.laptop-lid{left:180px;top:135px;width:840px;height:510px;background:#1c1c1c;border-radius:22px 22px 0 0;padding:28px 30px 0}
.laptop-screen{width:100%;height:100%;background:linear-gradient(180deg,#f4f4f4,#d9d9d9)}
.laptop-base{left:132px;top:645px;width:936px;height:28px;background:linear-gradient(#e8e8e8,#b4b4b4);border-radius:0 0 60px 60px}
.hero-kicker{left:0;top:688px;width:1200px;text-align:center;color:var(--white);font-size:24px;font-weight:300;letter-spacing:10px}
.hero-title{left:0;top:718px;width:1200px;text-align:center;color:var(--white);font-size:46px;font-weight:600;letter-spacing:9px;white-space:nowrap}
.dots{left:0;top:800px;width:1200px;display:flex;justify-content:center;gap:6px}
.dots span{width:22px;height:22px;border-radius:50%;background:var(--white)}
.dots span.off{background:transparent;border:3px solid var(--white)}

/* section labels */
.label{background:var(--black);color:var(--white);font-weight:700;font-size:44px;letter-spacing:6px;display:flex;align-items:center;justify-content:center;white-space:nowrap}

/* services */
.svc-title{color:var(--brand-dark);font-size:27px;font-weight:700;letter-spacing:3px;white-space:nowrap}
.svc-text{font-size:16.5px;line-height:1.4;color:#444;margin-top:26px}
.btn{display:inline-block;background:var(--brand);color:var(--white);font-size:15px;font-weight:700;letter-spacing:1px;padding:10px 24px;border-radius:24px}
.photo{background:linear-gradient(135deg,#cfd6de,#8e9aa6)}
.diamond{width:30px;height:30px;background:var(--brand);transform:rotate(45deg)}

/* wireless band */
.band{left:0;top:2445px;width:1200px;height:600px;background:linear-gradient(120deg,#7096cb,#4f7bb9 55%,#6d92c6)}
.feature{left:110px;display:flex;align-items:center;gap:30px}
.feature-icon{width:96px;height:96px;border-radius:50%;background:var(--black);display:flex;align-items:center;justify-content:center;color:var(--white);font-weight:700;font-size:44px;flex:none}
.feature h3{color:var(--white);font-size:30px;font-weight:700}
.feature p{color:var(--muted);font-size:16px;margin-top:6px}

/* help */
.help-intro{left:130px;top:3147px;width:940px;text-align:center;font-size:16.5px;line-height:1.5}
.mini-lid{left:118px;top:3240px;width:450px;height:270px;background:#1c1c1c;border-radius:14px 14px 0 0;padding:14px}
.mini-screen{width:100%;height:100%;background:var(--white);display:flex;align-items:center;justify-content:center;gap:12px}
.mini-base{left:96px;top:3510px;width:495px;height:18px;background:linear-gradient(#e6e6e6,#aaa);border-radius:0 0 40px 40px}
.help-title{left:612px;top:3245px;color:var(--brand-dark);font-size:30px;font-weight:700;letter-spacing:2px;white-space:nowrap}
.help-text{left:612px;top:3300px;width:470px;font-size:16.5px;line-height:1.45}
.help-list{left:612px;top:3395px;list-style:none;font-size:16.5px;line-height:1.55}
.help-list li::before{content:"";display:inline-block;width:8px;height:8px;border-radius:50%;background:var(--brand);margin-right:10px;vertical-align:middle}

/* clients */
.clients{left:0;top:3645px;width:1200px;height:495px;background:linear-gradient(120deg,#e6e9ee,#c4ccd6 50%,#dfe3e9)}
.client{width:204px;height:75px;background:rgba(255,255,255,.55);border:3px solid #333;display:flex;align-items:center;justify-content:center;font-size:26px;font-weight:600;color:#333}

/* footer */
.footer-bg{left:0;top:4140px;width:1200px;height:360px;background:var(--footer)}
.footer-col{color:var(--white)}
.footer-title{font-size:28px;font-weight:700;letter-spacing:3px;white-space:nowrap}
.footer-text{font-size:15px;line-height:1.4;margin-top:18px}
.footer-more{font-size:15px;font-weight:700;margin-top:26px}
.divider{top:4170px;width:2px;height:300px;background:var(--footer-line)}
.links{left:420px;top:4200px;list-style:none;color:var(--white)}
.links li{font-size:27px;font-weight:700;letter-spacing:3px;margin-bottom:14px;white-space:nowrap}
.contact-row{display:flex;align-items:flex-start;gap:12px;font-size:15px;margin-top:10px}
.social{width:58px;height:58px;border-radius:50%;background:var(--black);display:block}
</style>
</head>
<body>

<header>
  <div class="abs topbar"></div>
  <div class="abs brand-box">
    <span class="brand-mark"></span>
    <div><span class="brand-name">Velomor</span><span class="brand-tag">wireless internet</span></div>
  </div>
  <ul class="abs nav">
    <li class="active">HOME</li><li>SERVICES</li><li>ABOUT</li><li>OURWORK</li><li>CONTACT</li><li>PORTAL</li>
  </ul>
  <div class="abs phone">
    <svg width="18" height="18" viewBox="0 0 24 24"><path fill="#fff" d="M6.6 10.8a15 15 0 0 0 6.6 6.6l2.2-2.2c.3-.3.7-.4 1-.2 1.1.4 2.3.6 3.6.6.6 0 1 .4 1 1V20c0 .6-.4 1-1 1A17 17 0 0 1 3 4c0-.6.4-1 1-1h3.5c.6 0 1 .4 1 1 0 1.3.2 2.5.6 3.6.1.3 0 .7-.2 1z"/></svg>
    1300 555 014
  </div>
</header>

<section class="hero-section">
  <div class="abs hero"></div>
  <div class="abs laptop-lid"><div class="laptop-screen" role="img" aria-label="Illustration of silhouetted people using laptops and phones under wifi signals"></div></div>
  <div class="abs laptop-base"></div>
  <p class="abs hero-kicker">WELCOME TO</p>
  <h1 class="abs hero-title">VELOMOR WIRELESS INTERNET</h1>
  <div class="abs dots"><span></span><span class="off"></span><span></span></div>
</section>

<section class="services">
  <h2 class="abs label" style="left:375px;top:870px;width:450px;height:105px">OUR SERVICES</h2>

  <div class="abs" style="left:120px;top:990px;width:420px">
    <h3 class="svc-title">HOSPITALITY SOLUTIONS</h3>
    <p class="svc-text">Our high quality Wi Fi networks offer a robust 24/7 connectivity, enhancing our client's hospitality services. Whether travelling for business or pleasure, guests like to stay connected with their families, friends, and more importantly, with their work.</p>
    <div style="margin-top:40px;padding-left:108px"><span class="btn">READ MORE</span></div>
  </div>
  <div class="abs photo" style="left:600px;top:966px;width:501px;height:372px;background:linear-gradient(135deg,#eef1f5,#b8c3cf)" role="img" aria-label="Photo of a guest resting in bed using a tablet"></div>
  <div class="abs diamond" style="left:585px;top:1136px"></div>

  <div class="abs photo" style="left:99px;top:1341px;width:501px;height:366px;background:linear-gradient(135deg,#b48b6c,#5b4638)" role="img" aria-label="Photo of two people looking at a smartphone"></div>
  <div class="abs" style="left:639px;top:1372px;width:470px">
    <h3 class="svc-title">MOBILE SOUTIONS</h3>
    <p class="svc-text">Instant internet connectivity has become a basic need. No matter where someone travels, they expect it. Velomor applies its IT expertise to deliver a stable, reliable wireless solution in environments where the traditional broadband connection is not viable.</p>
    <div style="margin-top:40px;padding-left:100px"><span class="btn">READ MORE</span></div>
  </div>

  <div class="abs" style="left:140px;top:1730px;width:420px">
    <h3 class="svc-title">VELOMOR TV SOLUTIONS</h3>
    <p class="svc-text">The Velomor TV transforms the standard television into a complete information system. Guests can easily access essential hotel information from the home screen. Powered by Corvid OS, our smart TV also serves as a second, larger display screen for them to access their phone apps.</p>
    <div style="margin-top:30px;padding-left:84px"><span class="btn">READ MORE</span></div>
  </div>
  <div class="abs photo" style="left:639px;top:1728px;width:462px;height:330px;background:linear-gradient(135deg,#e8ebef,#7c8794)" role="img" aria-label="Photo of a hand pointing a remote at a television"></div>
  <div class="abs diamond" style="left:584px;top:1868px"></div>

  <div class="abs photo" style="left:99px;top:2058px;width:501px;height:330px;background:linear-gradient(135deg,#4f7a4a,#2c3b3a 60%,#7e8a8c)" role="img" aria-label="Photo of a modern office lounge with a green feature wall"></div>
  <div class="abs" style="left:639px;top:2080px;width:470px">
    <h3 class="svc-title">MINING AND REMOTE</h3>
    <p class="svc-text">At Velomor, we endeavour to connect the most remote and harsh locations with the rest of the world. Our systems are designed to offer an uninterrupted internet experience even in difficult environments, such as mining camps.</p>
    <div style="margin-top:38px;padding-left:105px"><span class="btn">READ MORE</span></div>
  </div>
</section>

<section class="wireless">
  <div class="abs band" role="img" aria-label="Blue-tinted photo of people working with devices"></div>
  <h2 class="abs label" style="left:300px;top:2391px;width:600px;height:102px">VELOMOR WIRELESS</h2>

  <div class="abs feature" style="top:2538px">
    <div class="feature-icon"><svg width="52" height="40" viewBox="0 0 52 40"><g fill="none" stroke="#fff" stroke-width="5" stroke-linecap="round"><path d="M4 14a31 31 0 0 1 44 0"/><path d="M12 22a20 20 0 0 1 28 0"/><path d="M20 30a9 9 0 0 1 12 0"/></g><circle cx="26" cy="36" r="3.5" fill="#fff"/></svg></div>
    <div><h3>Wi-Fi Hotspots</h3><p>Leading supplier of public access and internet billing systems.</p></div>
  </div>
  <div class="abs feature" style="top:2652px">
    <div class="feature-icon"><svg width="50" height="44" viewBox="0 0 50 44"><rect x="3" y="3" width="44" height="30" rx="3" fill="none" stroke="#fff" stroke-width="5"/><rect x="20" y="33" width="10" height="6" fill="#fff"/><rect x="13" y="39" width="24" height="4" fill="#fff"/></svg></div>
    <div><h3>Velomor tv</h3><p>Turn you standard TV into a full guest information system and point of sale.</p></div>
  </div>
  <div class="abs feature" style="top:2763px">
    <div class="feature-icon">H</div>
    <div><h3>HSIA Solutions</h3><p>Our guest access solutions have been built with the guest in mind and<br>are easy to use</p></div>
  </div>
  <div class="abs feature" style="top:2877px">
    <div class="feature-icon"><svg width="46" height="42" viewBox="0 0 46 42"><path d="M5 4h36a3 3 0 0 1 3 3v20a3 3 0 0 1-3 3H18l-9 8v-8H5a3 3 0 0 1-3-3V7a3 3 0 0 1 3-3z" fill="#fff"/></svg></div>
    <div><h3>Social Wi-Fi</h3><p>Get more out of your existing Wi-Fi with our social plug-ins to gain<br>valuble insight into users</p></div>
  </div>
</section>

<section class="help">
  <h2 class="abs label" style="left:324px;top:3015px;width:555px;height:105px">HOW CAN WE HELP</h2>
  <p class="abs help-intro">Lorem Ipsum is simply dummy text of the printing and typesetting industry. Lorem Ipsum has been the industry's standard dummy text ever since the 1500s</p>
  <div class="abs mini-lid"><div class="mini-screen"><span class="brand-mark"></span><div><span class="brand-name" style="font-size:58px">Velomor</span><span class="brand-tag" style="font-size:18px">wireless internet</span></div></div></div>
  <div class="abs mini-base"></div>
  <h3 class="abs help-title">VELOMOR SOLUTION</h3>
  <p class="abs help-text">Lorem Ipsum is simply dummy text of the printing and typesetting industry. Lorem Ipsum has been the industry's standard dummy text ever since the 1500s</p>
  <ul class="abs help-list"><li>Strong, Stable Network</li><li>Easy to use</li><li>Stay in Touch</li><li>Full support options</li></ul>
</section>

<section class="trusted">
  <div class="abs clients" role="img" aria-label="Soft photo of business people meeting"></div>
  <h2 class="abs label" style="left:240px;top:3591px;width:726px;height:108px">LIST OF TRUSTED CLIENTS</h2>
  <div class="abs client" style="left:168px;top:3810px">Lodgewell</div>
  <div class="abs client" style="left:392px;top:3810px">Tourkin</div>
  <div class="abs client" style="left:618px;top:3810px">Rovana</div>
  <div class="abs client" style="left:840px;top:3810px">Camptor</div>
  <div class="abs client" style="left:390px;top:3924px">Orevale</div>
  <div class="abs client" style="left:618px;top:3924px">Pantrel</div>
</section>

<footer>
  <div class="abs footer-bg"></div>
  <div class="abs footer-col" style="left:105px;top:4165px;width:270px">
    <h4 class="footer-title">ABOUT US</h4>
    <p class="footer-text">Velomor Wireless has been a leader in wireless networks and internet billing systems for over a decade. Velomor currently has completed over 2000 installations.</p>
    <p class="footer-more">MORE ›</p>
  </div>
  <div class="abs divider" style="left:393px"></div>
  <ul class="abs links">
    <li>› CASE STUDIES</li><li>› TESTIMONIALS</li><li>› NEWS</li><li>› RESELLERS</li>
  </ul>
  <div class="abs divider" style="left:762px"></div>
  <div class="abs footer-col" style="left:786px;top:4165px;width:380px">
    <h4 class="footer-title">CONTACT US</h4>
    <div class="contact-row" style="margin-top:18px">
      <svg width="14" height="20" viewBox="0 0 14 20"><path fill="#fff" d="M7 0a7 7 0 0 1 7 7c0 5-7 13-7 13S0 12 0 7a7 7 0 0 1 7-7zm0 4a3 3 0 1 0 0 6 3 3 0 0 0 0-6z"/></svg>
      <span>42 Harbour Crest Drive<br>Coral Bay, QLD 4400</span>
    </div>
    <div class="contact-row">
      <svg width="16" height="16" viewBox="0 0 24 24"><path fill="#fff" d="M6.6 10.8a15 15 0 0 0 6.6 6.6l2.2-2.2c.3-.3.7-.4 1-.2 1.1.4 2.3.6 3.6.6.6 0 1 .4 1 1V20c0 .6-.4 1-1 1A17 17 0 0 1 3 4c0-.6.4-1 1-1h3.5c.6 0 1 .4 1 1 0 1.3.2 2.5.6 3.6.1.3 0 .7-.2 1z"/></svg>
      <span>1300 555 014</span>
    </div>
    <div class="contact-row">
      <svg width="18" height="14" viewBox="0 0 18 14"><rect width="18" height="14" rx="1" fill="#fff"/><path d="M1 1l8 7 8-7" fill="none" stroke="#4f7fbf" stroke-width="1.6"/></svg>
      <span>sales@velomor.com.au</span>
    </div>
    <div style="display:flex;gap:12px;margin-top:26px;padding-left:10px">
      <span class="social" aria-label="Social profile"></span><span class="social" aria-label="Social profile"></span>
    </div>
  </div>
</footer>

</body>
</html>
```